Dinner Invitation for an email

Please create an image I can embed in an email. The tone should be sophisticated, fun and festive.

Here is the copy:

FOOD | FRIENDS | FUN
Please join BRV and friends at Corvetti's Harbor House for cocktails, conversation and a delectable dinner
Date: Monday, January 23 (during OPMI)
Time: Cocktails start at 6:30 | Dinner is around 7
Place: Corvetti's Harbor House - The Pearl Terrace
27318 W Dunmore Pkwy - Scottsdale
(Adjacent to the Halvorsen Pinecrest Lodge)

RSVP: mara.quinby@brvholdco.example
(Mara will send you a calendar invite)

Hope to see you there!

```html
<!DOCTYPE html>
<html lang="en">
<head>
<meta charset="utf-8">
<title>BRV Dinner Invitation</title>
<link href="https://fonts.googleapis.com/css2?family=Montserrat:wght@400;500;600;800&family=Bebas+Neue&family=Sacramento&display=swap" rel="stylesheet">
<style>
  :root {
    --page-bg: #e9ecef;
    --sky-light: #eafaff;
    --sky-mid: #d6f0fb;
    --navy: #0d3a9a;
    --royal: #1a6fce;
    --aqua: #5bc0e6;
    --ink: #333842;
    --rule: #3a3d44;
    --pin-red: #e53935;
    --leaf-green: #4caf50;
  }
  html, body {
    margin: 0;
    padding: 0;
    width: 980px;
    height: 1200px;
    overflow: hidden;
    background: var(--page-bg);
  }
  .invitation {
    position: absolute;
    left: 67px;
    top: 0;
    width: 846px;
    height: 1200px;
    overflow: hidden;
    background: radial-gradient(ellipse at 30% 20%, var(--sky-light) 0%, var(--sky-mid) 60%, var(--sky-light) 100%);
    font-family: "Montserrat", sans-serif;
    color: var(--ink);
  }
  .brand {
    position: absolute;
    top: 84px;
    left: 0;
    width: 100%;
    display: flex;
    justify-content: center;
    align-items: center;
    gap: 12px;
  }
  .brand-mark {
    width: 22px;
    height: 22px;
    background: var(--navy);
  }
  .brand-name {
    font-weight: 800;
    font-size: 60px;
    line-height: 1;
    color: var(--navy);
    letter-spacing: 1px;
  }
  .hero-illustration {
    position: absolute;
    left: 67px;
    top: 200px;
    width: 692px;
    height: 323px;
    border-radius: 160px 180px 0 0;
    background: linear-gradient(90deg, #6a4fd8 0%, #e8325a 22%, #f4f4f4 38%, #f5c400 55%, #2a2250 75%, #1f8fe8 100%);
    opacity: 0.85;
  }
  .headline {
    position: absolute;
    top: 566px;
    left: 0;
    width: 100%;
    text-align: center;
    font-weight: 800;
    font-size: 56px;
    line-height: 1;
    margin: 0;
    white-space: nowrap;
  }
  .headline .food { color: var(--navy); }
  .headline .friends { color: var(--royal); }
  .headline .fun { color: var(--aqua); }
  .headline .divider {
    color: var(--rule);
    font-weight: 400;
    font-size: 40px;
    vertical-align: 6px;
    margin: 0 14px;
  }
  .lead {
    position: absolute;
    top: 634px;
    left: 60px;
    width: 726px;
    text-align: center;
    font-size: 19px;
    font-weight: 600;
    line-height: 29px;
    margin: 0;
  }
  .details {
    position: absolute;
    top: 722px;
    left: 72px;
    width: 675px;
    height: 94px;
    border-top: 1.5px solid var(--rule);
    border-bottom: 1.5px solid var(--rule);
    display: flex;
    align-items: center;
    justify-content: center;
  }
  .detail {
    display: flex;
    align-items: center;
    gap: 10px;
  }
  .detail-label {
    font-family: "Bebas Neue", sans-serif;
    font-size: 46px;
    line-height: 1;
    color: var(--navy);
    padding-top: 4px;
  }
  .detail-text {
    font-size: 16px;
    font-weight: 600;
    line-height: 24px;
    margin-left: 8px;
  }
  .details-divider {
    width: 1.5px;
    height: 40px;
    background: var(--rule);
    margin: 0 10px 0 12px;
  }
  .place {
    position: absolute;
    top: 846px;
    left: 0;
    width: 100%;
    text-align: center;
  }
  .place-heading {
    display: flex;
    justify-content: center;
    align-items: center;
    gap: 10px;
  }
  .place-address {
    margin: 6px 0 0;
    font-size: 17.5px;
    font-weight: 500;
    line-height: 25px;
  }
  .place-note {
    margin: 2px 0 0;
    font-size: 11px;
    font-weight: 500;
  }
  .rsvp {
    position: absolute;
    top: 1000px;
    left: 0;
    width: 100%;
    text-align: center;
  }
  .rsvp-line {
    margin: 0;
    font-size: 18px;
    font-weight: 600;
    color: var(--navy);
  }
  .rsvp-note {
    margin: 4px 0 0;
    font-size: 17px;
    font-weight: 400;
  }
  .signoff {
    position: absolute;
    top: 1060px;
    left: 0;
    width: 100%;
    text-align: center;
    font-family: "Sacramento", cursive;
    font-size: 50px;
    line-height: 1.2;
    color: var(--ink);
    margin: 0;
  }
</style>
</head>
<body>
<main class="invitation">
  <div class="brand">
    <span class="brand-mark"></span>
    <span class="brand-name">BRV</span>
  </div>

  <div class="hero-illustration" role="img" aria-label="Illustration of four friends raising cocktail glasses among blue and purple leaves"></div>

  <h1 class="headline">
    <span class="food">FOOD</span><span class="divider">|</span><span class="friends">FRIENDS</span><span class="divider">|</span><span class="fun">FUN</span>
  </h1>

  <p class="lead">Please join BRV and friends at Corvetti's Harbor House for cocktails, conversation and a delectable dinner</p>

  <section class="details">
    <div class="detail">
      <svg width="34" height="34" viewBox="0 0 34 34" aria-hidden="true">
        <rect x="1" y="4" width="26" height="24" rx="2" fill="#fff" stroke="#555" stroke-width="1.5"/>
        <rect x="1" y="4" width="26" height="7" fill="var(--pin-red)"/>
        <circle cx="25" cy="25" r="7" fill="#fff" stroke="var(--royal)" stroke-width="2"/>
        <polyline points="25,21 25,25 28,26" fill="none" stroke="var(--royal)" stroke-width="1.5"/>
      </svg>
      <span class="detail-label">DATE</span>
      <span class="detail-text">Monday, January 23<br>(during OPMI)</span>
    </div>
    <span class="details-divider"></span>
    <div class="detail">
      <svg width="36" height="36" viewBox="0 0 36 36" aria-hidden="true">
        <circle cx="18" cy="18" r="16" fill="#fff" stroke="#2b2f36" stroke-width="2.5"/>
        <path d="M18 18 L18 5 A13 13 0 0 1 30 14 Z" fill="var(--aqua)"/>
        <polyline points="18,9 18,18 25,21" fill="none" stroke="var(--pin-red)" stroke-width="1.8"/>
      </svg>
      <span class="detail-label">TIME</span>
      <span class="detail-text">Cocktails start at 6:30<br>Dinner is around 7</span>
    </div>
  </section>

  <section class="place">
    <div class="place-heading">
      <svg width="30" height="34" viewBox="0 0 30 34" aria-hidden="true">
        <polygon points="2,30 10,24 20,24 28,30" fill="var(--leaf-green)"/>
        <path d="M15 2 C9 2 6 6 6 10 C6 16 15 26 15 26 C15 26 24 16 24 10 C24 6 21 2 15 2 Z" fill="var(--pin-red)"/>
        <circle cx="15" cy="10" r="3.5" fill="#fff"/>
      </svg>
      <span class="detail-label">PLACE</span>
    </div>
    <p class="place-address">Corvetti's Harbor House - The Pearl Terrace<br>27318 W Dunmore Pkwy - Scottsdale</p>
    <p class="place-note">(Adjacent to the Halvorsen Pinecrest Lodge)</p>
  </section>

  <section class="rsvp">
    <p class="rsvp-line">RSVP: mara.quinby@brvholdco.example</p>
    <p class="rsvp-note">(Mara will send you a calendar invite)</p>
  </section>

  <p class="signoff">Hope to see you there!</p>
</main>
</body>
</html>
```